Business Cards for a Junk Removal Company

Hello,
We are looking to have business cards designed that are simple, bold, easy to read, and right to the point. Please see the attachments for our logo files. We want the card to be yellow on both sides ( Color code Yellow: #FFE01B). The logo text font is (Rockstar Extra Bold) and this is also in the files attached. Please make the text black for the logo. On the back side of the card, you can use white and black for text. Thank you in advance for your hard work!

Front of card-
Harbor Haul Removal (logo)
Back of card-
Harbor Haul Removal
Donate - Recycle - Dispose
518-276-9053
www.harborhaulremoval.example
info@harborhaulremoval.example

Industry/Entity Type

Junk removal

Contact Information for Business Card

FRONT OF CARD- Harbor Haul Removal (logo) BACK OF CARD- Harbor Haul Removal Donate - Recycle - Dispose 518-276-9053 www.harborhaulremoval.example info@harborhaulremoval.example

Font styles to use
Other font styles liked:
• Rockstar Extra Bold

Colors
FFF300
FFF600
FEFA6F
FFFEC7
FFFEE8

Requirements
Must have
• Must have color code Yellow: #FFE01B for the background of front and back of the card

```html
<!DOCTYPE html>
<html lang="en">
<head>
<meta charset="utf-8">
<title>Harbor Haul Removal – Business Cards</title>
<link rel="stylesheet" href="https://fonts.googleapis.com/css2?family=Arimo:wght@400;700&display=swap">
<style>
  :root {
    --backdrop: #dcdcda;
    --card-yellow: #f0d443;
    --pattern-light: #ecce3c;
    --pattern-dark: #d9bb2c;
    --ink: #111111;
  }
  * { box-sizing: border-box; margin: 0; padding: 0; }
  html, body {
    width: 1200px; height: 801px; overflow: hidden;
    background: var(--backdrop);
  }
  .stage {
    width: 1200px; height: 801px;
    display: flex; align-items: center; justify-content: center; gap: 60px;
  }
  .card {
    position: relative;
    width: 520px; height: 297px;
    background: var(--card-yellow);
    font-family: "Arimo", Arial, sans-serif;
    color: var(--ink);
    overflow: hidden;
  }
  .card--info {
    display: flex; flex-direction: column; align-items: center;
    padding-top: 40px;
    text-align: center;
  }
  .brand-name {
    font-weight: 700;
    text-transform: uppercase;
    line-height: 1.02;
    letter-spacing: -0.3px;
  }
  .card--info .brand-name {
    font-size: 30px;
    margin-bottom: 26px;
  }
  .contact-line {
    font-size: 16px;
    line-height: 1.45;
  }
  .rule {
    width: 92px; height: 1.5px;
    background: var(--ink);
    margin: 14px 0 16px;
  }
  .tagline { font-size: 16px; }

  .card--pattern .pattern-fill {
    position: absolute; inset: 0;
    background:
      repeating-linear-gradient(-8deg, transparent 0 34px, rgba(0,0,0,0.035) 34px 58px),
      linear-gradient(135deg, var(--pattern-light) 0%, var(--pattern-dark) 100%);
  }
  .card--pattern .brand-name {
    position: absolute;
    left: 300px; top: 168px;
    font-size: 21px;
  }
</style>
</head>
<body>
<main class="stage">
  <section class="card card--info" aria-label="Card information side">
    <p class="brand-name">Harbor Haul<br>Removal</p>
    <p class="contact-line">518-276-9053</p>
    <p class="contact-line">www.harborhaulremoval.example</p>
    <p class="contact-line">info@harborhaulremoval.example</p>
    <div class="rule"></div>
    <p class="tagline">Donate - Recycle - Dispose</p>
  </section>

  <section class="card card--pattern" aria-label="Card brand side">
    <div class="pattern-fill" role="img" aria-label="Tone-on-tone repeating brand name texture covering the whole card"></div>
    <p class="brand-name">Harbor Haul<br>Removal</p>
  </section>
</main>
</body>
</html>
```